BriarLoom Website Homepage Design

Please provide your idea of homepage for a hosting company. This project is for DESIGN only, no coding.

It must use/combine colors used in logo, clean, modern look.

Homepage must consist of at least 4 sections (example: testimonials, services, and so on. not necesarily all of them). We would like the navigation to be horizontal, but not mandatory.

You can include a preview of services page (optional, not a must).

Number of Pages Required

1 page

Font styles to use
Sans Serif

```html
<!DOCTYPE html>
<html lang="en">
<head>
<meta charset="utf-8">
<title>BriarLoom — Hosting</title>
<link href="https://fonts.googleapis.com/css2?family=Poppins:wght@400;500;600;700&display=swap" rel="stylesheet">
<style>
:root{
  --blue:#0a5c94;
  --blue-dark:#084d7d;
  --gold:#c49a1c;
  --yellow:#f2c230;
  --grey:#9a9a9e;
  --ink:#3a3a3a;
  --line:#d6d6d6;
  --white:#ffffff;
  --pale:#cfe3f3;
}
*{box-sizing:border-box;margin:0;padding:0}
html,body{width:1200px;height:2446px;overflow:hidden;background:var(--white)}
body{position:relative;font-family:'Poppins',sans-serif;color:var(--ink)}
.abs{position:absolute}

/* header */
.site-header{position:absolute;left:0;top:0;width:1200px;height:50px;border-bottom:1px solid var(--line)}
.brand{position:absolute;left:178px;top:12px;font-weight:600;font-size:21px;color:var(--blue);letter-spacing:1px}
.main-nav{position:absolute;right:176px;top:18px;display:flex;gap:18px}
.main-nav a{font-size:10px;color:var(--blue);text-decoration:none;font-weight:500}
.main-nav a.active{font-weight:600;border-bottom:2px solid var(--blue);padding-bottom:5px}

/* hero */
.hero-card{left:257px;top:87px;width:689px;height:367px;border:1px solid var(--line);box-shadow:0 2px 5px rgba(0,0,0,.25);background:var(--white)}
.hero-art{left:33px;top:55px;width:232px;height:248px;border-radius:8px;background:linear-gradient(160deg,var(--pale),#8fbbe0)}
.hero-title{left:292px;top:20px;width:380px;font-size:15.5px;line-height:24px;font-weight:700;color:var(--blue)}
.hero-list{left:337px;top:118px;list-style:none}
.hero-list li{display:flex;align-items:center;gap:8px;font-size:11.5px;height:30.5px;color:var(--ink)}
.hero-btn{left:385px;top:311px;width:228px;height:31px;border-radius:8px;background:var(--blue);color:var(--white);font-size:11.5px;font-weight:600;display:flex;align-items:center;justify-content:center}

/* section heads */
.section-title{left:178px;font-size:21px;font-weight:600;color:var(--blue);letter-spacing:.2px}

/* pricing */
.billing-toggle{left:470px;top:539px;width:260px;height:42px;border-radius:21px;background:var(--blue);display:flex;align-items:center;padding-left:10px;color:var(--white);font-size:11.5px;font-weight:500}
.billing-toggle span{padding:0 10px}
.billing-toggle .on{background:var(--gold);height:34px;border-radius:17px;display:flex;align-items:center;margin-right:2px}
.plan{top:623px;width:261px;height:300px;border:1px solid #c9c9c9;box-shadow:0 1px 3px rgba(0,0,0,.2);text-align:center;background:var(--white)}
.plan-band{height:32px;background:var(--grey);color:var(--white);font-size:11.5px;font-weight:600;display:flex;align-items:center;justify-content:center}
.plan.featured .plan-band{background:var(--blue)}
.plan-name{margin-top:6px;font-size:18px;font-weight:500;color:var(--gold)}
.plan-desc{margin:4px auto 0;width:238px;font-size:6px;line-height:9px;text-align:left;color:var(--ink)}
.plan-price{margin-top:18px;font-size:20px;color:#111}
.plan-price b{font-weight:600}
.plan-features{list-style:none;margin:18px 0 0 44px;text-align:left}
.plan-features li{display:flex;align-items:center;gap:6px;height:20.7px;font-size:11.5px;font-weight:500;color:var(--blue)}
.plan-btn{position:absolute;left:23px;bottom:13px;width:215px;height:30px;border-radius:15px;background:var(--grey);color:var(--white);font-size:15px;font-weight:500;display:flex;align-items:center;justify-content:center}
.plan.featured .plan-btn{background:var(--blue)}

/* services copy */
.copy{font-size:13.2px;line-height:18.8px;color:var(--ink)}
.copy.justify{text-align:justify}
.services-art{left:686px;top:1228px;width:332px;height:340px;border-radius:6px;background:linear-gradient(180deg,#ececec 0%,#f3d36a 55%,#e2e2e2 100%)}

/* additional services */
.extras{left:178px;top:1775px;width:846px;height:96px;border:1.5px solid #cfcfcf;border-radius:12px;box-shadow:0 1px 3px rgba(0,0,0,.15)}
.extra{position:absolute;top:12px;width:140px;margin-left:-70px;text-align:center}
.extra-icon{width:42px;height:42px;margin:0 auto;border:1.5px solid var(--gold);border-radius:50%;display:flex;align-items:center;justify-content:center}
.extra-label{margin-top:12px;font-size:9.5px;font-weight:500;color:var(--blue)}

/* faq */
.faq-item{left:178px;width:845px;height:53px;background:var(--blue);border-left:5px solid var(--yellow);color:var(--white);font-size:10.5px;font-weight:500;line-height:17px}
.faq-item p{position:absolute;left:20px;top:10px;width:640px}
.faq-item svg{position:absolute;right:112px;top:20px}

/* footer */
.site-footer{left:0;top:2245px;width:1200px;height:201px;background:var(--blue);color:var(--white)}
.footer-brand{position:absolute;left:0;width:1200px;top:10px;text-align:center;font-size:19px;font-weight:600;letter-spacing:1px}
.footer-col{position:absolute;top:55px}
.footer-col h4{font-size:9.5px;font-weight:500;margin-bottom:5px}
.footer-col li{list-style:none;font-size:7px;line-height:16.2px;padding-left:11px}
.footer-social{position:absolute;right:177px;top:55px;text-align:right}
.footer-social h4{font-size:9.5px;font-weight:500}
.social-dots{display:flex;gap:12px;justify-content:flex-end;margin-top:14px}
.social-dots span{width:15px;height:15px;border-radius:50%;background:var(--white)}
</style>
</head>
<body>

<header class="site-header">
  <div class="brand">BriarLoom</div>
  <nav class="main-nav">
    <a class="active">SERIVICES</a><a>PRICES</a><a>ACCOMMODATION</a><a>DOMAINS</a><a>E-MAIL</a>
  </nav>
</header>

<section class="abs hero-card">
  <div class="abs hero-art" role="img" aria-label="Isometric illustration of a laptop, cloud upload and server rack"></div>
  <h1 class="abs hero-title">LOREM IPSUM DOLOR SIT AMET, CONSECTETUR ADIPISCING ELIT.</h1>
  <ul class="abs hero-list">
    <li><svg width="13" height="10" viewBox="0 0 13 10"><path d="M1 5l4 4 7-8" fill="none" stroke="#c49a1c" stroke-width="2.2"/></svg>aenean vitae bibendum urna, non gravida massa.</li>
    <li><svg width="13" height="10" viewBox="0 0 13 10"><path d="M1 5l4 4 7-8" fill="none" stroke="#c49a1c" stroke-width="2.2"/></svg>aenean vitae bibendum urna, non gravida massa.</li>
    <li><svg width="13" height="10" viewBox="0 0 13 10"><path d="M1 5l4 4 7-8" fill="none" stroke="#c49a1c" stroke-width="2.2"/></svg>aenean vitae bibendum urna, non gravida massa.</li>
    <li><svg width="13" height="10" viewBox="0 0 13 10"><path d="M1 5l4 4 7-8" fill="none" stroke="#c49a1c" stroke-width="2.2"/></svg>aenean vitae bibendum urna, non gravida massa.</li>
  </ul>
  <div class="abs hero-btn">LOREM IPSUM DOLOR</div>
</section>

<h2 class="abs section-title" style="top:493px">PLANS AND PRICES</h2>
<div class="abs billing-toggle"><span class="on">MONTHLY</span><span>QUARTERLY</span><span>ANNUAL</span></div>

<article class="abs plan" style="left:178px">
  <div class="plan-band"></div>
  <div class="plan-name">PLAN 1</div>
  <p class="plan-desc">there is no one who loves pain itself, who seeks after it and wants to have it, simply because it is pain...</p>
  <div class="plan-price"><b>US$ 99.00/</b>month</div>
  <ul class="plan-features">
    <li><svg width="9" height="12"><path d="M2 1l5 5-5 5" fill="none" stroke="#c49a1c" stroke-width="2.2"/></svg>lorem ipsum dolor sit amet</li>
    <li><svg width="9" height="12"><path d="M2 1l5 5-5 5" fill="none" stroke="#c49a1c" stroke-width="2.2"/></svg>lorem ipsum dolor sit amet</li>
    <li><svg width="9" height="12"><path d="M2 1l5 5-5 5" fill="none" stroke="#c49a1c" stroke-width="2.2"/></svg>lorem ipsum dolor sit amet</li>
    <li><svg width="9" height="12"><path d="M2 1l5 5-5 5" fill="none" stroke="#c49a1c" stroke-width="2.2"/></svg>lorem ipsum dolor sit amet</li>
  </ul>
  <div class="plan-btn">For trial for 30 days</div>
</article>

<article class="abs plan featured" style="left:470px">
  <div class="plan-band">MOST CHOSEN</div>
  <div class="plan-name">PLAN 2</div>
  <p class="plan-desc">there is no one who loves pain itself, who seeks after it and wants to have it, simply because it is pain...</p>
  <div class="plan-price"><b>US$ 99.00/</b>month</div>
  <ul class="plan-features">
    <li><svg width="9" height="12"><path d="M2 1l5 5-5 5" fill="none" stroke="#c49a1c" stroke-width="2.2"/></svg>lorem ipsum dolor sit amet</li>
    <li><svg width="9" height="12"><path d="M2 1l5 5-5 5" fill="none" stroke="#c49a1c" stroke-width="2.2"/></svg>lorem ipsum dolor sit amet</li>
    <li><svg width="9" height="12"><path d="M2 1l5 5-5 5" fill="none" stroke="#c49a1c" stroke-width="2.2"/></svg>lorem ipsum dolor sit amet</li>
    <li><svg width="9" height="12"><path d="M2 1l5 5-5 5" fill="none" stroke="#c49a1c" stroke-width="2.2"/></svg>lorem ipsum dolor sit amet</li>
  </ul>
  <div class="plan-btn">For trial for 30 days</div>
</article>

<article class="abs plan" style="left:762px">
  <div class="plan-band"></div>
  <div class="plan-name">PLAN 3</div>
  <p class="plan-desc">there is no one who loves pain itself, who seeks after it and wants to have it, simply because it is pain...</p>
  <div class="plan-price"><b>US$ 99.00/</b>month</div>
  <ul class="plan-features">
    <li><svg width="9" height="12"><path d="M2 1l5 5-5 5" fill="none" stroke="#c49a1c" stroke-width="2.2"/></svg>lorem ipsum dolor sit amet</li>
    <li><svg width="9" height="12"><path d="M2 1l5 5-5 5" fill="none" stroke="#c49a1c" stroke-width="2.2"/></svg>lorem ipsum dolor sit amet</li>
    <li><svg width="9" height="12"><path d="M2 1l5 5-5 5" fill="none" stroke="#c49a1c" stroke-width="2.2"/></svg>lorem ipsum dolor sit amet</li>
    <li><svg width="9" height="12"><path d="M2 1l5 5-5 5" fill="none" stroke="#c49a1c" stroke-width="2.2"/></svg>lorem ipsum dolor sit amet</li>
  </ul>
  <div class="plan-btn">For trial for 30 days</div>
</article>

<h2 class="abs section-title" style="top:963px">SERVICES</h2>
<p class="abs copy" style="left:192px;top:1022px;width:745px">Lorem ipsum dolor sit amet, consectetur adipiscing elit. Aenean vitae bibendum urna, non gravida massa. In sagittis odio a dapibus vulputate. Mauris luctus nisl erat. Praesent sollicitudin libero vel consectetur efficitur. Nam a quam rutrum, lobortis mi et, eleifend turpis. Quisque aliquet tellus quis porta molestie. Curabitur id magna a lectus pharetra dignissim. Mauris vitae velit turpis. Donec sit amet eleifend eros, ut rutrum ligula. Praesent quis vehicula dui, sit amet posuere orci. Vestibulum lacinia hendrerit lacus.</p>
<p class="abs copy" style="left:192px;top:1135px;width:745px">Lorem ipsum dolor sit amet, consectetur adipiscing elit. Aenean vitae bibendum urna, non gravida massa. In sagittis odio a dapibus vulputate. Mauris luctus nisl erat. Praesent sollicitudin libero vel consectetur efficitur. Nam a quam rutrum, lobortis mi et, eleifend turpis. Quisque aliquet tellus quis porta molestie. Curabitur id magna a lectus pharetra dignissim. Mauris vitae velit turpis. Donec sit amet eleifend eros, ut rutrum ligula. Praesent quis vehicula dui, sit amet posuere orci. Vestibulum lacinia hendrerit lacus.</p>
<p class="abs copy justify" style="left:192px;top:1248px;width:451px">Lorem ipsum dolor sit amet, consectetur adipiscing elit. Aenean vitae bibendum urna, non gravida massa. Insagittis odio a dapibus vulputate. Mauris luctus nisl erat. Praesent sollicitudin libero vel consectetur efficitur. Nam a quamrutrum, lobortis mi et, eleifend turpis. Quisque aliquet tellus quis porta molestie. Curabitur id magna a lectus pharetra dignissim. Mauris vitae velit turpis. Donec sit amet eleifend eros, ut rutrum ligula. Praesent quis vehicula dui, sit amet posuere orci. Vestibulum lacinia hendrerit lacus.</p>
<p class="abs copy justify" style="left:192px;top:1417px;width:451px">Lorem ipsum dolor sit amet, consectetur adipiscing elit. Aenean vitae bibendum urna, non gravida massa. Insagittis odio a dapibus vulputate. Mauris luctus nisl erat. Praesent sollicitudin libero vel consectetur efficitur. Nam a quamrutrum, lobortis mi et, eleifend turpis. Quisque aliquet tellus quis porta molestie. Curabitur id magna a lectus pharetra dignissim. Mauris vitae velit turpis. Donec sit amet eleifend eros, ut rutrum ligula. Praesent quis vehicula dui, sit amet posuere orci. Vestibulum lacinia hendrerit lacus.</p>
<div class="abs services-art" role="img" aria-label="Illustration of a woman leaning on a large phone showing a yellow login screen, beside a potted plant"></div>
<p class="abs copy justify" style="left:192px;top:1587px;width:733px">Lorem ipsum dolor sit amet, consectetur adipiscing elit. Aenean vitae bibendum urna, non gravida massa. Insagittis odio a dapibus vulputate. Mauris luctus nisl erat. Praesent sollicitudin libero vel consectetur efficitur. Nam a quamrutrum, lobortis mi et, eleifend turpis. Quisque aliquet tellus quis porta molestie. Curabitur id magna a lectus pharetra dignissim. Mauris vitae velit turpis. Donec sit amet eleifend eros, ut rutrum ligula. Praesent quis vehicula dui, sit amet posuere orci. Vestibulum lacinia hendrerit lacus.</p>

<h2 class="abs section-title" style="top:1722px">ADDITIONAL &nbsp;SERVICES</h2>
<section class="abs extras">
  <div class="extra" style="left:107px">
    <div class="extra-icon"><svg width="20" height="20" viewBox="0 0 20 20" fill="#c49a1c"><rect x="1" y="2" width="18" height="4.5" rx="1"/><rect x="1" y="7.8" width="18" height="4.5" rx="1"/><rect x="1" y="13.6" width="18" height="4.5" rx="1"/></svg></div>
    <div class="extra-label">ACCOMODATION</div>
  </div>
  <div class="extra" style="left:315px">
    <div class="extra-icon" style="color:var(--gold);font-size:22px;font-weight:700">$</div>
    <div class="extra-label">PLANS</div>
  </div>
  <div class="extra" style="left:534px">
    <div class="extra-icon"><svg width="18" height="20" viewBox="0 0 18 20" fill="#c49a1c"><ellipse cx="9" cy="4" rx="8" ry="3"/><path d="M1 6.5c0 1.7 3.6 3 8 3s8-1.3 8-3V10c0 1.7-3.6 3-8 3s-8-1.3-8-3z"/><path d="M1 12.5c0 1.7 3.6 3 8 3s8-1.3 8-3V16c0 1.7-3.6 3-8 3s-8-1.3-8-3z"/></svg></div>
    <div class="extra-label">DATABASE</div>
  </div>
  <div class="extra" style="left:754px">
    <div class="extra-icon"><svg width="20" height="15" viewBox="0 0 20 15"><rect x="0" y="0" width="20" height="15" rx="2" fill="#c49a1c"/><path d="M1 1.5l9 6.5 9-6.5" fill="none" stroke="#fff" stroke-width="1.5"/></svg></div>
    <div class="extra-label">EMAIL</div>
  </div>
</section>

<h2 class="abs section-title" style="top:1910px">RECURRING DOUBTS</h2>
<div class="abs faq-item" style="top:1960px"><p>LOREM IPSUM DOLOR SIT AMET, CONSECTETUR ADIPISCING ELIT. AENEAN VITAE BIBENDUM URNA, NON GRAVIDA MASSA.</p><svg width="14" height="9"><path d="M1.5 1.5l5.5 5.5 5.5-5.5" fill="none" stroke="#fff" stroke-width="2.2"/></svg></div>
<div class="abs faq-item" style="top:2024px"><p style="top:18px">LOREM IPSUM DOLOR SIT AMET, CONSECTETUR ADIPISCING ELIT.</p><svg width="14" height="9"><path d="M1.5 1.5l5.5 5.5 5.5-5.5" fill="none" stroke="#fff" stroke-width="2.2"/></svg></div>
<div class="abs faq-item" style="top:2089px"><p>LOREM IPSUM DOLOR SIT AMET, CONSECTETUR ADIPISCING ELIT. AENEAN VITAE BIBENDUM URNA, NON GRAVIDA MASSA.</p><svg width="14" height="9"><path d="M1.5 1.5l5.5 5.5 5.5-5.5" fill="none" stroke="#fff" stroke-width="2.2"/></svg></div>
<div class="abs faq-item" style="top:2154px"><p>LOREM IPSUM DOLOR SIT AMET.</p><svg width="14" height="9"><path d="M1.5 1.5l5.5 5.5 5.5-5.5" fill="none" stroke="#fff" stroke-width="2.2"/></svg></div>

<footer class="abs site-footer">
  <div class="footer-brand">BriarLoom</div>
  <div class="footer-col" style="left:178px"><h4>LOREM IPSUM</h4><ul><li>CONSECTETUR ADIPISCING</li><li>CONSECTETUR ADIPISCING</li><li>CONSECTETUR ADIPISCING</li><li>CONSECTETUR ADIPISCING</li><li>CONSECTETUR ADIPISCING</li></ul></div>
  <div class="footer-col" style="left:372px"><h4>LOREM IPSUM</h4><ul><li>CONSECTETUR ADIPISCING</li><li>CONSECTETUR ADIPISCING</li><li>CONSECTETUR ADIPISCING</li><li>CONSECTETUR ADIPISCING</li><li>CONSECTETUR ADIPISCING</li></ul></div>
  <div class="footer-col" style="left:567px"><h4>LOREM IPSUM</h4><ul><li>CONSECTETUR ADIPISCING</li><li>CONSECTETUR ADIPISCING</li><li>CONSECTETUR ADIPISCING</li><li>CONSECTETUR ADIPISCING</li><li>CONSECTETUR ADIPISCING</li></ul></div>
  <div class="footer-col" style="left:762px"><h4>LOREM IPSUM</h4><ul><li>CONSECTETUR ADIPISCING</li><li>CONSECTETUR ADIPISCING</li><li>CONSECTETUR ADIPISCING</li><li>CONSECTETUR ADIPISCING</li><li>CONSECTETUR ADIPISCING</li></ul></div>
  <div class="footer-social"><h4>LOREM IPSUM</h4><div class="social-dots"><span></span><span></span><span></span><span></span></div></div>
</footer>

</body>
</html>
```